Wine Label Design for a white wine made in the region of San Gimignano, Italy

This is a white wine (crisp and fresh) that is made in the region of San Gimignano, Italy, which is a beautiful hill town in Tuscany famous for it's towers. We would like a classy, elegant front wine label that can also be somewhat fun and whimsical if you prefer. Showcasing or depicting or alluding to the town and the towers of San Gimignano is a plus. The label should state the brand name which is "Vellisora", the varietal, which is Vernaccia di San Gimignano, and the vintage which is 2015. We might change the size of the label slightly but for design purposes please use 5 inches wide x 5 1/2 inches tall. I've uploaded a photo of a successful label design for parameters, but you should not feel limited to this either. Good white wine colors are white and green but we are flexible. Please don't use red, burgundy, or blue colors.

Target Market(s)

This wine label should appeal to all ages but be classy for the older crowd and still eye catching and fun for the millennials. This wine is sold in 15 states in the US, on the East Coast.

Industry/Entity Type

Town

Font styles to use
Serif
Sans Serif

Requirements
Must have
• Referring somehow or depicting the hill town and towers of San Gimignano in some way, such as in silhouette would be a plus. But also try to do something fun and unique with it-- not just an image of the town with words placed over it.
Should not have
• Please don't use the colors blue, reds. Try to think about what makes a wine label classy and sophisticated and 'upmarket' and what makes one cheap and cheesy. We are looking for the classy and sophisticated.

```html
<!DOCTYPE html>
<html lang="en">
<head>
<meta charset="utf-8">
<title>Vellisora – Vernaccia di San Gimignano Label</title>
<link href="https://fonts.googleapis.com/css2?family=Cormorant+Garamond:wght@500;600&family=Raleway:wght@200;300&display=swap" rel="stylesheet">
<style>
  :root {
    --page: #ffffff;
    --frame-line: #8a8a8a;
    --leaf-green: #6e8936;
    --leaf-green-deep: #5f7a2c;
    --slate: #45463e;
    --mark-box: #494a44;
    --copper-dark: #9b5d27;
    --copper-mid: #c98a45;
    --copper-light: #ecc98a;
    --hill-light: #c8c9b4;
    --hill-mid: #a4a692;
    --hill-dark: #818373;
    --gold-text: #c9a15a;
    --gold-text-dark: #a87a3a;
    --ink: #1d1b18;
    --vintage: #f1f0ea;
  }
  * { margin: 0; padding: 0; box-sizing: border-box; }
  html, body {
    width: 1200px; height: 1000px; overflow: hidden;
    background: var(--page);
  }
  .canvas { position: relative; width: 1200px; height: 1000px; }

  .label-sheet {
    position: absolute; left: 336px; top: 210px;
    width: 528px; height: 581px;
    border: 1px solid var(--frame-line);
    background: var(--page);
  }
  .label {
    position: absolute; left: 90px; top: 0;
    width: 346px; height: 579px;
    background: var(--slate);
    overflow: hidden;
  }
  .label__pattern {
    position: absolute; left: 0; top: 0;
    width: 346px; height: 290px;
    background: radial-gradient(circle at 50% 40%, var(--leaf-green) 0%, var(--leaf-green-deep) 100%);
  }
  .label__mark-box {
    position: absolute; left: 122px; top: 0;
    width: 71px; height: 131px;
    background: var(--mark-box);
    display: flex; align-items: center; justify-content: center;
  }
  .label__mark-name {
    font-family: "Raleway", sans-serif;
    font-weight: 300;
    font-size: 12px;
    letter-spacing: 1px;
    color: var(--copper-light);
  }
  .label__brand-band {
    position: absolute; left: 0; top: 151px;
    width: 346px; height: 47px;
    background: linear-gradient(90deg, var(--copper-dark) 0%, var(--copper-mid) 20%, var(--copper-light) 48%, var(--copper-mid) 78%, var(--copper-dark) 100%);
    display: flex; align-items: center; justify-content: center;
  }
  .label__brand-name {
    font-family: "Raleway", sans-serif;
    font-weight: 200;
    font-size: 37px;
    letter-spacing: 1px;
    color: var(--ink);
    text-transform: uppercase;
    line-height: 1;
  }
  .label__hills {
    position: absolute; left: 0; top: 222px;
    width: 346px; height: 120px;
    background: linear-gradient(180deg, var(--hill-light) 0%, var(--hill-mid) 55%, var(--hill-dark) 100%);
  }
  .label__varietal {
    position: absolute; left: 0; top: 372px; width: 346px;
    text-align: center;
    font-family: "Cormorant Garamond", serif;
    font-weight: 600;
    font-variant: small-caps;
    color: var(--gold-text);
    line-height: 1;
  }
  .label__varietal-line { display: block; font-size: 31px; letter-spacing: 1px; }
  .label__varietal-joint { display: block; font-size: 22px; margin: 2px 0 1px; }
  .label__vintage {
    position: absolute; left: 0; top: 487px; width: 346px;
    text-align: center;
    font-family: "Raleway", sans-serif;
    font-weight: 200;
    font-size: 32px;
    color: var(--vintage);
  }
</style>
</head>
<body>
  <main class="canvas">
    <section class="label-sheet">
      <div class="label">
        <div class="label__pattern" role="img" aria-label="Fine green interlaced ornamental pattern"></div>
        <div class="label__mark-box">
          <span class="label__mark-name">Vellisora</span>
        </div>
        <div class="label__brand-band">
          <h1 class="label__brand-name">Vellisora</h1>
        </div>
        <div class="label__hills" role="img" aria-label="Layered silhouette of Tuscan hills in soft sage greys"></div>
        <p class="label__varietal">
          <span class="label__varietal-line">Vernaccia</span>
          <span class="label__varietal-joint">di</span>
          <span class="label__varietal-line">San Gimignano</span>
        </p>
        <p class="label__vintage">2016</p>
      </div>
    </section>
  </main>
</body>
</html>
```